Tending Our Garden eBook Cover Design

I want to deisgn a cover for my eBook (FRONT COVER) and the title is:

Under the Willow Tree; Where I Found My Quiet Strength and Where You Might Too
By KT Dorran

TITLE CHANGED TO: UNDER THE WILLOW TREE; WHERE I FOUND MY QUIET STRENGTH AND WHERE YOU MIGHT TOO

The color palette is attached. Along with some photos options of me. Along with the ebook in WORD Document. My website is www.KTDorranLive.example. You can use a different color palette if you think it is best

Target Market(s)

women who look to build a personal brand

Industry/Entity Type

health and wellness

Requirements
Must have
• the title
Nice to have
• use my picture on the cover; but that is optional
Should not have
• any men

```html
<!DOCTYPE html>
<html lang="en">
<head>
<meta charset="utf-8">
<title>Under the Willow Tree — KT Dorran</title>
<link href="https://fonts.googleapis.com/css2?family=League+Spartan:wght@600;700&display=swap" rel="stylesheet">
<style>
  :root {
    --backdrop: #000000;
    --rose: #efa0a8;
    --blush: #fde0e6;
    --wine: #5e272d;
    --white: #ffffff;
    --photo-dark: #1c1416;
    --photo-mid: #6b4a45;
  }
  html, body {
    margin: 0;
    padding: 0;
    width: 1200px;
    height: 1080px;
    overflow: hidden;
    background: var(--backdrop);
  }
  .canvas {
    position: relative;
    width: 1200px;
    height: 1080px;
  }
  .cover {
    position: absolute;
    left: 276px;
    top: 53px;
    width: 648px;
    height: 972px;
    overflow: hidden;
    background: var(--rose);
  }
  .cover-art {
    position: absolute;
    inset: 0;
    width: 648px;
    height: 972px;
  }
  .title-line,
  .subtitle-line,
  .author-name {
    font-family: "League Spartan", sans-serif;
    font-weight: 700;
    text-transform: uppercase;
  }
  .title-line,
  .subtitle-line { fill: var(--wine); }
  .author-name {
    fill: var(--white);
    stroke: var(--wine);
    stroke-width: 1;
    paint-order: stroke;
  }
</style>
</head>
<body>
<div class="canvas">
  <div class="cover">
    <svg class="cover-art" viewBox="0 0 648 972" xmlns="http://www.w3.org/2000/svg">
      <defs>
        <linearGradient id="photo-tone" x1="0" y1="0" x2="0" y2="1">
          <stop offset="0" stop-color="var(--photo-mid)"/>
          <stop offset="0.45" stop-color="var(--photo-dark)"/>
          <stop offset="1" stop-color="var(--photo-dark)"/>
        </linearGradient>
      </defs>

      <polygon class="title-panel" points="260,0 388,0 648,186 648,389 0,389 0,186"
               fill="var(--blush)" stroke="var(--wine)" stroke-width="1"/>
      <path class="subtitle-pill" d="M648,509 H461 A96,96 0 0 0 461,701 H648 Z"
            fill="var(--blush)" stroke="var(--wine)" stroke-width="1"/>

      <path class="author-photo" role="img"
            aria-label="Photo of the author, smiling, in a black turtleneck and dark trousers, raising one hand"
            d="M18,972 L18,544 A150,150 0 0 1 168,394 L221,394 A150,150 0 0 1 371,544 L371,720 L275,860 L275,972 Z"
            fill="url(#photo-tone)"/>

      <text class="title-line" x="324" y="120" text-anchor="middle" font-size="46">Under the</text>
      <text class="title-line" x="324" y="202" text-anchor="middle" font-size="62">Willow Tree</text>
      <text class="title-line" x="324" y="280" text-anchor="middle" font-size="38">Where I Found My</text>
      <text class="title-line" x="324" y="344" text-anchor="middle" font-size="38">Quiet Strength</text>

      <text class="subtitle-line" x="596" y="567" text-anchor="end" font-size="32">And Where</text>
      <text class="subtitle-line" x="596" y="613" text-anchor="end" font-size="32">You Might</text>
      <text class="subtitle-line" x="596" y="659" text-anchor="end" font-size="32">Too</text>

      <text class="author-name" x="596" y="923" text-anchor="end" font-size="44">By KT Dorran</text>
    </svg>
  </div>
</div>
</body>
</html>
```